Stationery Design Project

QV7 Staffing requires letterhead and business card designs for a company based in London. Just like the name, we're a management resourcing company, providing resources to third party companies. You can see www.qv7staffing-example.com for ideas on existing colour schemes and design concepts that have been implimented and agreed to. Ultimately the design should broadcast professionalism, safety and the concept of growth.

Target Market(s)

Financial institutes; friendly societies (All UK based)

Industry/Entity Type

Safety

Requirements
Must have
• Files produced should be print ready; and the text in them editable (eg address, name etc)

```html
<!DOCTYPE html>
<html lang="en">
<head>
<meta charset="utf-8">
<title>QV7 Staffing — Stationery</title>
<link rel="stylesheet" href="https://fonts.googleapis.com/css2?family=Open+Sans:wght@300;400;600&family=PT+Sans:wght@400&display=swap">
<style>
  :root {
    --backdrop: #ececec;
    --paper: #ffffff;
    --teal-dark: #2f7f7c;
    --teal-light: #7dbfcc;
    --card-blue: #38a3bd;
    --card-blue-light: #7fcadb;
    --ink: #2b2b2b;
    --ink-soft: #8a8a8a;
    --signature-tone: #ededed;
  }
  * { box-sizing: border-box; margin: 0; padding: 0; }
  html, body { width: 1200px; height: 900px; overflow: hidden; }
  body {
    background: var(--backdrop);
    position: relative;
    font-family: "Open Sans", sans-serif;
  }

  .wordmark {
    display: flex;
    align-items: center;
    gap: 8px;
    font-family: "Open Sans", sans-serif;
    font-weight: 600;
    color: var(--teal-dark);
    white-space: nowrap;
  }
  .wordmark__square { background: var(--teal-dark); flex: none; }

  /* Letterhead */
  .letterhead {
    position: absolute;
    left: 94px; top: 36px;
    width: 612px; height: 792px;
    background: var(--paper);
  }
  .letterhead .wordmark {
    position: absolute; left: 28px; top: 58px;
    font-size: 26px;
  }
  .letterhead .wordmark__square { width: 20px; height: 20px; }

  .letter-body {
    position: absolute;
    left: 97px; top: 190px;
    width: 447px;
    font-family: "PT Sans", sans-serif;
    font-size: 9.4px;
    line-height: 10.4px;
    color: var(--ink);
    text-align: justify;
  }
  .letter-body p + p { margin-top: 10.4px; }

  .signature {
    position: absolute;
    left: 100px; top: 583px;
    width: 100px; height: 72px;
    background: var(--signature-tone);
  }

  .letter-footer {
    position: absolute;
    left: 0; top: 697px;
    height: 77px;
    padding-left: 25px;
    border-left: 14px solid var(--teal-light);
    font-size: 9px;
    line-height: 13px;
    font-weight: 300;
    color: #555;
    display: flex; flex-direction: column; justify-content: center;
    padding-left: 11px;
  }
  .letter-footer .label { color: var(--teal-light); }
  .letter-footer .web { font-weight: 400; letter-spacing: 0.4px; }
  .letter-footer .web strong { color: var(--teal-light); font-weight: 400; }

  /* Business cards */
  .card {
    position: absolute;
    width: 254px; height: 145px;
    border-radius: 0 20px 0 20px;
    overflow: hidden;
  }
  .card--front {
    left: 775px; top: 215px;
    background: var(--paper);
    border: 1px solid #d9d9d9;
  }
  .card--front .wordmark {
    position: absolute; left: 12px; top: 22px;
    font-size: 15px; gap: 6px;
  }
  .card--front .wordmark__square { width: 12px; height: 12px; }

  .card__address {
    position: absolute; left: 22px; top: 78px;
    font-size: 6px; line-height: 9px; font-weight: 300; color: var(--ink-soft);
  }
  .card__person {
    position: absolute; right: 22px; top: 87px;
    text-align: right;
  }
  .card__name { font-size: 9.5px; font-weight: 600; color: var(--teal-dark); line-height: 12px; }
  .card__role { font-size: 6px; font-weight: 300; color: var(--ink-soft); }
  .card__tab {
    position: absolute; right: 0; top: 84px;
    width: 10px; height: 28px;
    background: var(--teal-light);
  }
  .card__contacts {
    position: absolute; left: 22px; top: 103px;
    list-style: none;
    font-size: 6px; line-height: 8.6px; font-weight: 300; color: var(--ink-soft);
  }
  .card__contacts li { display: flex; align-items: center; gap: 5px; }
  .card__contacts svg { width: 7px; height: 7px; fill: var(--teal-light); flex: none; }

  .card--back {
    left: 778px; top: 378px;
    background: radial-gradient(circle at 50% 30%, var(--card-blue-light) 0%, var(--card-blue) 60%, #2f97b1 100%);
  }
  .card--back .wordmark {
    position: absolute; left: 10px; top: 112px;
    font-size: 17px; color: #ffffff; gap: 6px;
  }
  .card--back .wordmark__square { width: 13px; height: 13px; background: #ffffff; }
</style>
</head>
<body>

<section class="letterhead">
  <div class="wordmark"><span class="wordmark__square"></span>QV7 Staffing</div>

  <div class="letter-body">
    <p>Lorem ipsum dolor sit amet, consectetuer adipiscing elit. Pellentesque tristique elementum sem. Quisque eget erat ac lectus sodales faucibus. Nam commodo est. Cras consequat faucibus velit. Nam ac magna. Sed et ligula. Nam volutpat, elit ac facilisis tempor, neque augue euismod leo, sit amet molestie sem est eu libero. Nulla facilisi. Pellentesque sit amet odio. Curabitur a leo consectetuer leo blandit porttitor. Pellentesque velit quam, gravida at, pharetra eu, convallis non, sem. Aenean tempor nibh at purus. Pellentesque porta. Suspendisse congue, lacus sit amet imperdiet imperdiet, urna massa rutrum urna, id elementum tellus diam quis risus.</p>
    <p>In dui turpis, varius vitae, tincidunt id, consequat ut, leo. Donec tincidunt tristique odio. Nulla erat felis, euismod nec, fringilla non, aliquet et, magna. Nulla at magna quis nisi pretium vehicula. Pellentesque habitant morbi tristique senectus et netus et malesuada fames ac turpis egestas. Class aptent taciti sociosqu ad litora torquent per conubia nostra, per inceptos himenaeos. In vel quam. Phasellus varius convallis purus. In non turpis. Nam sed risus. Etiam non neque at nisl gravida porttitor. Donec leo dolor, feugiat ut, pharetra et, porttitor a, metus. Suspendisse laoreet magna vel elit. Ut est augue, fermentum ac, molestie at, vestibulum et, urna.</p>
    <p>Nunc purus. Cras auctor. In ornare neque id ipsum. Nulla tincidunt, diam sit amet viverra euismod, sapien augue fringilla neque, at pellentesque felis tortor vel enim. Etiam dignissim. Sed a tortor vel nisl euismod ultricies. Donec molestie congue lectus. Integer sed turpis a tortor imperdiet consequat. Maecenas molestie placerat urna. Sed pede enim, sollicitudin nec, pretium nec, sollicitudin a, felis. In hac habitasse platea dictumst. Nam facilisis, tellus non scelerisque placerat, turpis turpis semper ante, euismod imperdiet augue nisi et neque. Vivamus tincidunt.</p>
    <p>Nulla lobortis ultricies nulla. Pellentesque purus mi, consequat quis, hendrerit sed, imperdiet non, eros. Nullam urna est, vehicula nec, cursus nec, dignissim sit amet, risus. Duis molestie, tellus sit amet laoreet ullamcorper, urna nisi fringilla ante, at rhoncus justo dolor vel dui. Nam hendrerit luctus lorem. Aenean tempor, metus vel posuere gravida, arcu nunc imperdiet tellus, ut blandit sem magna a turpis. Vivamus in neque. Lorem ipsum dolor sit amet, consectetuer adipiscing elit. Duis tristique tortor id nisl feugiat posuere. Maecenas posuere nisi ac risus. Nunc hendrerit. Praesent porta tempus ligula. Morbi in leo. Curabitur sapien nulla, cursus eget, faucibus in, porttitor et, odio. Praesent sed justo sed arcu commodo feugiat. Duis facilisis nulla ut eros. Cras libero. Donec mollis consectetuer metus. Praesent odio.</p>
  </div>

  <div class="signature" role="img" aria-label="Handwritten signature of the sender"></div>

  <footer class="letter-footer">
    <span>48 Harbour Lane, Suite</span>
    <span>Kestrel Bay, KB&nbsp; 40512</span>
    <span><span class="label">Phone.</span> 555-201-4830</span>
    <span><span class="label">Fax.</span> 555-201-4830</span>
    <span class="web">www.<strong>qv7staffing-example</strong>.com</span>
  </footer>
</section>

<section class="card card--front">
  <div class="wordmark"><span class="wordmark__square"></span>QV7 Staffing</div>
  <div class="card__address">48 Harbour Lane, Suite 2<br>Kestrel Bay, KB&nbsp; 40512</div>
  <div class="card__person">
    <div class="card__name">Daniel Marsh</div>
    <div class="card__role">Marketing Manager</div>
  </div>
  <div class="card__tab"></div>
  <ul class="card__contacts">
    <li><svg viewBox="0 0 10 10"><path d="M2 1h2l1 2-1.2 1a5 5 0 0 0 2.2 2.2L7 5l2 1v2c0 .6-.5 1-1 1A8 8 0 0 1 1 2c0-.5.4-1 1-1z"/></svg>0044 (0)300 555 0142</li>
    <li><svg viewBox="0 0 10 10"><rect x="1" y="6" width="2" height="3"/><rect x="4" y="4" width="2" height="5"/><rect x="7" y="1" width="2" height="8"/></svg>0044 (0)7700 555 218</li>
    <li><svg viewBox="0 0 10 10"><rect x="2" y="1" width="6" height="3"/><rect x="1" y="4" width="8" height="4" rx="1"/><rect x="3" y="7" width="4" height="2"/></svg>0044 (0)300 555 0149</li>
    <li><svg viewBox="0 0 10 10"><path d="M1 2h8v6H1z M1 2l4 3 4-3" fill="none" stroke="#7dbfcc" stroke-width="1"/></svg>info@qv7staffing-example.com</li>
  </ul>
</section>

<section class="card card--back">
  <div class="wordmark"><span class="wordmark__square"></span>QV7 Staffing</div>
</section>

</body>
</html>
```